New modern and animated Design needed for a portal login site (Relaymark Portal)

Relaymark is software for market communication B2B & EAI.
We need a modern look for a Relaymark Portal login site. We prefer a full size use for the background design of the login-page, with animation.
The name of the site is “Relaymark Langzeitarchiv”, what should appear as text. Further there is space needed for the login name and password.
Responsive Design is required.
We have a new Relaymark logo (find attached), that can be used for the animation, for example but not necessarily.
Feel free to visit our website for inspiration (colours etc.): www.vornelsystems.de.

Reason: Can you please animate the backgraound and send links to view it.

Reason: there is aproblem with pitchforge - we acually cannot view any designs

Target Market(s)

energy sector, IT

Industry/Entity Type

Communication

Number of Pages Required

1 page

Font styles to use
Sans Serif

Colors

Designer to choose colors to be used in the design.

Requirements
Must have
• fullscreen background design (like "onepager"),
• animated (infinity), not to much action
• the only text that is needed is "Relaymark Langzeitarchiv" (in front) and the login details: "Benutzername" (+ space for the username (free position)) and "Paswort" (+ space for the password (free position))
Nice to have
• maybe shades of blue, or colours, like the ones used on our website and logo (vornel systems) or Relaymark icon (files named "asset")
• animation can also be a film that starts over and over again (note: The up half of the page www.mirtobanu.de is one example, which is nice to watch - but here it is not necessary to use a movie)

```html
<!DOCTYPE html>
<html lang="de">
<head>
<meta charset="utf-8">
<title>Relaymark Langzeitarchiv – Login</title>
<link rel="stylesheet" href="https://fonts.googleapis.com/css2?family=Raleway:wght@400;500;700&display=swap">
<style>
  :root {
    --sky-deep: #0f5fc4;
    --sky-mid: #1d8fe0;
    --sky-light: #3cc6f0;
    --glow: #8fdcff;
    --card: #ffffff;
    --accent: #2aa9e0;
    --brand-navy: #1f4f9c;
    --rule: #e3e6ea;
    --btn-grey: #e7e8ea;
    --btn-grey-text: #3a4766;
    --btn-blue: #0b8fd0;
    --btn-blue-text: #ffffff;
  }
  * { box-sizing: border-box; margin: 0; padding: 0; }
  html, body {
    width: 1200px;
    height: 675px;
    overflow: hidden;
  }
  body {
    font-family: "Raleway", Arial, sans-serif;
    position: relative;
  }
  .backdrop {
    position: absolute;
    inset: 0;
    background:
      radial-gradient(ellipse 60% 14% at 75% 48%, rgba(143,220,255,0.55), transparent 70%),
      radial-gradient(ellipse 55% 16% at 18% 46%, rgba(143,220,255,0.45), transparent 70%),
      radial-gradient(ellipse 80% 40% at 60% 8%, rgba(60,198,240,0.9), transparent 70%),
      linear-gradient(180deg, var(--sky-light) 0%, var(--sky-mid) 40%, var(--sky-mid) 60%, var(--sky-deep) 100%);
  }
  .login-card {
    position: absolute;
    left: 374px;
    top: 192px;
    width: 503px;
    height: 331px;
    background: var(--card);
    box-shadow: 0 6px 24px rgba(10, 50, 110, 0.25);
  }
  .brand {
    position: absolute;
    left: 38px;
    top: 30px;
    display: flex;
    align-items: center;
    gap: 14px;
  }
  .brand-dot {
    width: 52px;
    height: 52px;
    border-radius: 50%;
    background: var(--brand-navy);
  }
  .brand-name {
    color: var(--brand-navy);
    font-size: 16px;
    font-weight: 500;
    line-height: 15px;
    letter-spacing: 0.4px;
  }
  .partner-name {
    position: absolute;
    right: 33px;
    top: 40px;
    color: var(--brand-navy);
    font-size: 16px;
    font-weight: 500;
    letter-spacing: 0.2px;
  }
  .field {
    position: absolute;
    left: 42px;
    width: 417px;
    height: 22px;
    border-bottom: 1px solid var(--rule);
  }
  .field-user { top: 111px; }
  .field-pass { top: 164px; }
  .field-label {
    display: block;
    color: var(--accent);
    font-size: 11.5px;
    font-weight: 500;
    letter-spacing: 1px;
  }
  .forgot-link {
    position: absolute;
    top: 214px;
    left: 0;
    width: 100%;
    text-align: center;
    color: var(--accent);
    font-size: 11.5px;
    font-weight: 500;
    letter-spacing: 1px;
    text-decoration: none;
  }
  .actions {
    position: absolute;
    left: 0;
    bottom: 0;
    width: 100%;
    height: 50px;
    display: flex;
  }
  .btn {
    display: flex;
    align-items: center;
    font-family: inherit;
    font-size: 11.5px;
    font-weight: 700;
    letter-spacing: 1.2px;
    border: 0;
  }
  .btn-register {
    width: 252px;
    padding-left: 19px;
    background: var(--btn-grey);
    color: var(--btn-grey-text);
  }
  .btn-login {
    flex: 1;
    justify-content: flex-end;
    padding-right: 19px;
    background: var(--btn-blue);
    color: var(--btn-blue-text);
  }
</style>
</head>
<body>
  <div class="backdrop" role="img" aria-label="Soft blue background with a glowing band of blurred light particles"></div>

  <main class="login-card">
    <div class="brand">
      <span class="brand-dot"></span>
      <span class="brand-name">relaymark<br>langzeitarchiv</span>
    </div>
    <span class="partner-name">vornel systems</span>

    <div class="field field-user"><span class="field-label">BENUTZERNAME</span></div>
    <div class="field field-pass"><span class="field-label">PASSWORT</span></div>

    <a class="forgot-link" href="#">PASSWORT VERGESSEN?</a>

    <div class="actions">
      <span class="btn btn-register">REGISTRIEREN</span>
      <span class="btn btn-login">EINLOGGEN</span>
    </div>
  </main>
</body>
</html>
```